Starter & Alternator business needs a website

update: very good designs submitted so far. also need this to display well on mobile devices. not sure if wordpress or html/css is better for my needs.

Our existing website is vellumtorq.com and is need of total revamp. Need full design of a website for my business.

We sell and rebuild starters and alternators. Customers bring in the units and we rebuild them. Or we sell them brand new or rebuilt units we have in stock. We do not install units into vehicles like a mechanic would. We strictly rebuild starters and alternators in our shop, sell brand new units over the counter, and we do deliver occasionally as well. We do offer a line of Orvan batteries as well but that is only a small feature of the business.

I would like this website designed and coded. I can upload the files to my web host after completion. I can also add in and modify content like our background info, etc.

I have included an illustrator file that shows some of our signage and logo, etc. I have also included a radio commercial sample so you can get a little better feel for the business. A similar ad does run on the radio currently, slightly different and without the added sound effects.

Update: I do like using photos of real items(starters or alternators etc) for an icon, like a real alternator stock image for the alternator section icon, etc. Maybe incorporate our logo in that design as well. That looks nice as well and may aid in navigation.

For any other design elements, do what you think looks good. Our colors are red/white/blue as seen in the illustrator file. our building is painted with halbeck moray colors, ember gala red and deep tide for blue.

Here are some examples of rebuilders websites in other markets for reference:

https://quillmarauto.com/starter-alternator-rebuilding/

https://www.dunwickmotorworks.com/auto-repairs/alternator-starter-rebuilds.aspx

https://www.fjordvoltage.com/

https://www.pemberlowgx.com/

The website can have areas for: services and products offered, high output alternators, Orvan Batteries, troubleshooting tips, current specials, contact info and directions/map, etc. Whatever else you feel applies.

At some point I do want to be able to sell items directly online or at least have a secure section for customers to submit invoice payments, but that's not necessarily in scope for this project just something to keep in mind.

Target Market(s)

Mechanics and Managers in fleet shops, construction and marine industries, shipping trades. Also automobile owners who work on their own vehicles. We sell and rebuild starters and alternators for automobiles, heavy duty equipment, forklifts, traxlifts, man movers, ferrettes, loaders, large tractors and trucks, just about any engine, golf carts, generators, etc.

Industry/Entity Type

Automotive Part

Coding

Coded - Design and coding required

Number of Pages Required

5+ page

Font styles to use
Serif
Sans Serif

Colors
0255a3
ec1f27
ffffff

Requirements
Must have
• Should also display nicely on mobile phones. Highlight our specialty, "Starters & Alternators"

```html
<!DOCTYPE html>
<html lang="en">
<head>
<meta charset="utf-8">
<title>Vellumtorq Starters &amp; Alternators</title>
<link href="https://fonts.googleapis.com/css2?family=Lato:wght@400;700;900&display=swap" rel="stylesheet">
<style>
:root{
  --blue:#0a3c8c;
  --blue-deep:#0255a3;
  --red:#e1002a;
  --red-soft:#ec1f27;
  --ink:#333;
  --muted:#555;
  --grey-bg:#e9e9e9;
  --footer-bg:#f2f2f2;
  --white:#fff;
}
*{margin:0;padding:0;box-sizing:border-box}
html,body{width:1200px;height:3458px;overflow:hidden}
body{position:relative;font-family:'Lato',sans-serif;color:var(--ink);background:var(--white)}
.abs{position:absolute}
.hero{left:0;top:70px;width:1200px;height:640px;background:linear-gradient(120deg,#5b6068 0%,#2c2f35 45%,#15171b 100%)}
.header-cut{left:0;top:0;width:1200px;height:170px}
.logo{left:172px;top:22px;width:280px}
.logo-row{display:flex;align-items:center;gap:10px}
.logo-dot{width:44px;height:44px;border:3px solid var(--blue);border-radius:50%;flex:none}
.logo-name{font-weight:900;font-size:27px;color:var(--blue);letter-spacing:.5px}
.logo-phone{margin-top:8px;display:flex;align-items:center;gap:8px;font-weight:900;font-size:27px;color:var(--red)}
.logo-phone::before,.logo-phone::after{content:"";flex:1;height:2px;background:var(--red)}
.logo-tag{margin-top:6px;font-size:9px;font-weight:900;color:var(--blue)}
.nav{left:562px;top:22px;display:flex;gap:28px;font-size:17px;color:#333}
.cart{left:995px;top:19px;width:32px;height:32px;border-radius:50%;background:var(--red)}
.cart svg{display:block;margin:8px auto}
.hero-title{left:310px;top:325px;display:flex;align-items:center;gap:18px}
.hero-ring{width:120px;height:120px;border:4px solid var(--white);border-radius:50%}
.hero-text{font-weight:900;font-size:64px;line-height:58px;color:var(--white);letter-spacing:1px}
.dots{left:526px;top:648px;display:flex;gap:4px}
.dots span{width:34px;height:4px;background:#cfd2d6}
.services-bg{left:0;top:710px;width:1200px;height:600px;background:var(--grey-bg)}
.section-title{width:1200px;left:0;text-align:center;font-weight:900;font-size:31px;letter-spacing:-.5px}
.section-title .blue{color:var(--blue)} .section-title .red{color:var(--red)}
.svc-card{top:840px;width:272px;height:370px;background:var(--white);border:1px solid #d8d8d8;text-align:center}
.svc-card.lift{box-shadow:0 8px 20px rgba(0,0,0,.15)}
.svc-img{height:198px}
.svc-card h3{margin-top:20px;font-size:16px;color:var(--blue);font-weight:700}
.svc-card p{margin:14px auto 0;width:236px;font-size:11px;line-height:19px;color:var(--muted)}
.btn{display:inline-block;margin-top:18px;background:var(--red);color:var(--white);font-size:11px;font-weight:700;padding:6px 15px;border-radius:14px}
.specials{left:0;top:1270px;width:1200px;height:650px}
.spec-card{top:1482px;width:202px;height:303px;background:var(--white);text-align:center}
.spec-img{margin:15px auto 0;width:170px;height:150px;border-radius:8px}
.spec-card h3{margin-top:22px;font-size:16px;color:var(--blue);font-weight:700}
.spec-card p{margin:10px auto 0;width:180px;font-size:11px;line-height:19px;color:var(--muted)}
.price{margin-top:12px;font-size:14px;color:var(--red)}
.blog-h{font-size:20px;color:#111;font-weight:400;line-height:23px}
.blog-p{font-size:11px;line-height:19px;color:var(--muted)}
.blog-date{font-size:12px;font-weight:900;color:var(--red)}
.map{left:0;top:2733px;width:1200px;height:440px;background:linear-gradient(135deg,#eef0ee,#e2e5e3 60%,#ececec)}
.contact{left:172px;top:2611px;width:855px;height:319px;background:var(--red);border-radius:14px;color:var(--white);text-align:center}
.contact h2{margin-top:50px;font-size:30px;font-weight:900;letter-spacing:-.5px}
.contact .lead{margin-top:18px;font-size:14px;font-weight:700}
.contact .sub{margin-top:6px;font-size:11px}
.contact hr{border:0;border-top:1px solid rgba(255,255,255,.55);margin-top:32px}
.info{position:absolute;top:215px;display:flex;align-items:center;gap:12px;text-align:left;font-size:11px;line-height:21px}
.info-ico{width:34px;height:34px;border:2px solid var(--white);border-radius:50%;flex:none;display:flex;align-items:center;justify-content:center}
.footer{left:0;top:3172px;width:1200px;height:286px;background:var(--footer-bg)}
.f-head{font-size:16px;color:#222}
.f-links{font-size:11px;line-height:20px;color:#333}
.email{left:769px;top:3268px;width:172px;height:34px;background:var(--white);border:1px solid #ccc;font-size:11px;padding:10px 8px}
.signup{left:941px;top:3268px;width:86px;height:34px;background:var(--blue);color:var(--white);font-size:12px;font-weight:700;text-align:center;padding-top:10px}
.social{left:769px;top:3330px;display:flex;gap:22px}
.social span{width:16px;height:16px;border-radius:50%;background:#333}
.cards{left:769px;top:3414px;display:flex;gap:7px}
.cards span{width:37px;height:23px;border-radius:3px;border:1px solid #ccc;background:var(--white)}
.cards span:nth-child(3){background:#2a5aa8}
.copy{left:172px;top:3420px;font-size:11px;color:#333}
</style>
</head>
<body>

<div class="abs hero" role="img" aria-label="Close-up photograph of an alternator mounted in an engine bay"></div>
<svg class="abs" style="left:0;top:660px" width="1200" height="60"><polygon points="0,60 1200,20 1200,60" fill="var(--grey-bg)"/><polygon points="560,60 1200,0 1200,20 560,60" fill="var(--red)"/></svg>
<svg class="abs header-cut" width="1200" height="170"><polygon points="0,0 1200,0 1200,70 552,70 470,162 0,162" fill="var(--white)"/></svg>

<div class="abs logo">
  <div class="logo-row"><span class="logo-dot"></span><span class="logo-name">VELLUMTORQ</span></div>
  <div class="logo-phone">555-0142</div>
  <div class="logo-tag">Automotive / Marine / Heavy Duty &nbsp; 1450 Kelmora Ave</div>
</div>
<nav class="abs nav"><span>Home</span><span>Services</span><span>Specials</span><span>Articles</span><span>Contact</span></nav>
<div class="abs cart"><svg width="16" height="16" viewBox="0 0 16 16"><path d="M1 2h3l2 8h7l2-6H5" fill="none" stroke="#fff" stroke-width="2"/><circle cx="7" cy="13" r="1.5" fill="#fff"/><circle cx="12" cy="13" r="1.5" fill="#fff"/></svg></div>

<div class="abs hero-title"><div class="hero-ring"></div><div class="hero-text">STARTERS &amp;<br>ALTERNATORS</div></div>
<div class="abs dots"><span></span><span></span><span></span><span></span></div>

<section>
  <div class="abs services-bg"></div>
  <h2 class="abs section-title" style="top:772px"><span class="blue">SERVICES AND </span><span class="red">PRODUCTS OFFERED</span></h2>
  <div class="abs svc-card" style="left:172px"><div class="svc-img" role="img" aria-label="Photo of a high output alternator" style="background:linear-gradient(135deg,#9aa0a6,#3b4047)"></div><h3>High Output Alternators</h3><p>Lorem ipsum dolor sit amet, consectedipis cing elit, sed do eiusmod tempor incididunut labore et dolore magna aliquim aini.m</p><span class="btn">Read More</span></div>
  <div class="abs svc-card lift" style="left:465px"><div class="svc-img" role="img" aria-label="Photo of a battery being fitted into a vehicle" style="background:linear-gradient(135deg,#6c7077,#1f2226)"></div><h3>Orvan Batteries</h3><p>Lorem ipsum dolor sit amet, consectedipis cing elit, sed do eiusmod tempor incididunut labore et dolore magna aliquim aini.m</p><span class="btn">Read More</span></div>
  <div class="abs svc-card" style="left:756px"><div class="svc-img" role="img" aria-label="Photo of a mechanic tightening an engine pulley with a wrench" style="background:linear-gradient(135deg,#7a7f86,#2d3036)"></div><h3>Troubleshooting tips</h3><p>Lorem ipsum dolor sit amet, consectedipis cing elit, sed do eiusmod tempor incididunut labore et dolore magna aliquim aini.m</p><span class="btn">Read More</span></div>
</section>

<section>
  <svg class="abs specials" width="1200" height="650" viewBox="0 0 1200 650"><defs><linearGradient id="spec-grad" x1="0" x2="1"><stop offset="0" stop-color="#0a3c8c"/><stop offset="1" stop-color="#e1002a"/></linearGradient></defs><polygon points="0,0 1200,85 1200,620 0,650" fill="url(#spec-grad)"/></svg>
  <h2 class="abs section-title" style="top:1404px;color:var(--white)">CURRENT SPECIALS</h2>
  <div class="abs spec-card" style="left:172px"><div class="spec-img" role="img" aria-label="Product photo of an alternator" style="background:radial-gradient(#c9ccd0,#f4f4f4)"></div><h3>Product Name</h3><p>Lorem ipsum dolor sit ameete dipiscing elit, sed do eius.</p><div class="price">$ 250.00</div></div>
  <div class="abs spec-card" style="left:390px"><div class="spec-img" role="img" aria-label="Product photo of a starter motor" style="background:radial-gradient(#b9bcc1,#f4f4f4)"></div><h3>Product Name</h3><p>Lorem ipsum dolor sit ameete dipiscing elit, sed do eius.</p><div class="price">$ 250.00</div></div>
  <div class="abs spec-card" style="left:607px"><div class="spec-img" role="img" aria-label="Product photo of an alternator" style="background:radial-gradient(#a9adb3,#f4f4f4)"></div><h3>Product Name</h3><p>Lorem ipsum dolor sit ameete dipiscing elit, sed do eius.</p><div class="price">$ 250.00</div></div>
  <div class="abs spec-card" style="left:824px"><div class="spec-img" role="img" aria-label="Product photo of a starter motor" style="background:radial-gradient(#8d9197,#f4f4f4)"></div><h3>Product Name</h3><p>Lorem ipsum dolor sit ameete dipiscing elit, sed do eius.</p><div class="price">$ 250.00</div></div>
</section>

<section>
  <h2 class="abs section-title" style="top:2016px"><span class="blue">LATEST </span><span class="red">BLOG</span></h2>
  <div class="abs" role="img" aria-label="Photo of an alternator on an engine" style="left:172px;top:2088px;width:415px;height:269px;background:linear-gradient(135deg,#8e949b,#2f3338)"></div>
  <h3 class="abs blog-h" style="left:172px;top:2376px">Lorem ipsum dolor sit amet,consectetur</h3>
  <p class="abs blog-p" style="left:172px;top:2410px;width:400px">Sed ut perspiciatis undloree omnis iste natus error sit voluptatem accusaloren tium doloremque laudantium, totloram rem aperiam, eaque ipsa.</p>
  <div class="abs blog-date" style="left:172px;top:2458px">JUNE 28 2019</div>

  <div class="abs" role="img" aria-label="Photo of a hand attaching a red clamp to a car battery" style="left:605px;top:2088px;width:206px;height:180px;background:linear-gradient(135deg,#3a3f46,#141619)"></div>
  <h3 class="abs blog-h" style="left:828px;top:2096px;width:200px">Lorem ipsum dolor sit amet,consectetur</h3>
  <p class="abs blog-p" style="left:828px;top:2148px;width:200px">Sed ut perspiciatis undloree omnis iste natus error sit voluptatem accusaloren tium doloremque laudantium, totloram rem aperiam, eaque ipsa.</p>
  <div class="abs blog-date" style="left:831px;top:2236px">JUNE 28 2019</div>

  <div class="abs" role="img" aria-label="Photo of an alternator close-up" style="left:605px;top:2293px;width:206px;height:179px;background:linear-gradient(135deg,#7d838a,#1e2125)"></div>
  <h3 class="abs blog-h" style="left:828px;top:2300px;width:200px">Lorem ipsum dolor sit amet,consectetur</h3>
  <p class="abs blog-p" style="left:828px;top:2352px;width:200px">Sed ut perspiciatis undloree omnis iste natus error sit voluptatem accusaloren tium doloremque laudantium, totloram rem aperiam, eaque ipsa.</p>
  <div class="abs blog-date" style="left:831px;top:2440px">JUNE 28 2019</div>
</section>

<section>
  <div class="abs map" role="img" aria-label="Street map showing the shop location"></div>
  <div class="abs contact">
    <h2>CONTACT INFO AND DIRECTIONS</h2>
    <p class="lead">Your source for New and High-Quality Rebuilt Starters &amp; Alternators.</p>
    <p class="sub">Serving the Marine, Heavy Duty, Specialty, and Automotive industries.</p>
    <hr>
    <div class="info" style="left:58px"><span class="info-ico"><svg width="14" height="16" viewBox="0 0 14 16"><path d="M7 1a5 5 0 0 0-5 5c0 4 5 9 5 9s5-5 5-9a5 5 0 0 0-5-5z" fill="none" stroke="#fff" stroke-width="1.6"/><circle cx="7" cy="6" r="1.7" fill="#fff"/></svg></span><span>Stop by at 1450 Kelmora Ave, Harrowvale, ST 00000.<br>Located in Brenmoor near Perrin &amp; Kelmora.</span></div>
    <div class="info" style="left:418px"><span class="info-ico"><svg width="16" height="16" viewBox="0 0 16 16"><path d="M3 2l3 0 1 3-2 1.5a8 8 0 0 0 4.5 4.5L11 9l3 1v3c-6 1-12-5-11-11z" fill="#fff"/></svg></span><span>Call us Today at<br>555-201-0142</span></div>
    <div class="info" style="left:590px"><span class="info-ico"><svg width="16" height="16" viewBox="0 0 16 16"><circle cx="8" cy="8" r="6" fill="none" stroke="#fff" stroke-width="1.6"/><path d="M8 4.5V8h2.5" fill="none" stroke="#fff" stroke-width="1.6"/></svg></span><span>Our hours of operation are<br>Mon-Fri 7-5pm, Sat 8-1pm.</span></div>
  </div>
</section>

<footer>
  <div class="abs footer"></div>
  <div class="abs logo" style="top:3225px">
    <div class="logo-row"><span class="logo-dot"></span><span class="logo-name">VELLUMTORQ</span></div>
    <div class="logo-phone">555-0142</div>
    <div class="logo-tag">Automotive / Marine / Heavy Duty &nbsp; 1450 Kelmora Ave</div>
  </div>
  <div class="abs f-head" style="left:558px;top:3230px">Links</div>
  <div class="abs f-links" style="left:561px;top:3266px">Home<br>Testimonial<br>Shop<br>About us</div>
  <div class="abs f-head" style="left:769px;top:3230px">Newsletter</div>
  <div class="abs email">Email:</div>
  <div class="abs signup">SIGN UP</div>
  <div class="abs social"><span></span><span></span><span></span><span></span></div>
  <div class="abs copy">© 2019 All Rights Are Reserved.Terms of Use | Privacy Policy</div>
  <div class="abs cards"><span></span><span></span><span></span><span></span><span></span><span></span></div>
</footer>

</body>
</html>
```